Flyer für Führungskräfte-Workshops und Coaching
Wir waren von der Zusammenarbeit begeistert. Petra hat sich von Anfang an intensiv mit dem Inhalt auseinandergesetzt und uns schon beim ersten kreativen Vorschlag überzeugt. Die Detailarbeit bis zum finalen Entwurf lief professionell und zügig. So arbeiten wir am liebsten. Professionell, sympathisch, klar und zuverlässig. Wir gebe eine ganz klare Empfehlung.
Zielgruppe
Firma/Organisation: norquavo - Personal- und Unternehmensberatung
Wir sind eine (zweiköpfige) Personal- und Unternehmensberatung aus der Hamburger Speicherviertel, die Coachings, Trainings und moderierte Workshops für Fach- und Führungskräfte anbietet.
Zielgruppe:
• Mittelstandsunternehmen
• Geschäftsführer
• Fach- und Führungskräfte
Aufgabenstellung
Ziel des Flyers:
• Kompetenz in den Bereichen Training, Workshop und Coaching vermitteln
• Flyer soll auf Fachmessen eingesetzt werden (Kaltakquise)
• Gesprächsanlässe für den Erstkontakt mit norquavo
Kernbotschaften:
• Weiterentwicklung von Fach- und Führungskräften in Richtung Wirksamkeit
• Zwei Säulen: Haltung und Führungshandwerk
• Firmenindividuelle Konzeption, praxisnah, relevant, abwechslungsreich
• Wertschätzender Umgang, Fokus auf Teilnehmer-Schwerpunkte
Tonalität:
• Professionell + sympathisch + praktisch/pragmatisch/natürlich
Gestaltung:
• Schwerpunkt auf grafische Elemente
• Wenig Text
• Integration von Logo und Grundfarben von norquavo
• Unkonventionelle Gestaltung, Abgrenzung von der Konkurrenz
Themenbeispiele:
• Umgang mit Verschiedenheit
• Konfliktfähigkeit
• Prozessentwicklung/-optimierung
• Führungshandwerk
• Mitarbeiterführung
• Coaching
• Selbstmanagement
• Zeitmanagement
• Schlagfertigkeit
• Unternehmenskultur
Format:
• DIN A4, 1-fach-Faltung, Endformat DIN A5 (Alternativen möglich)
Bildmaterial:
• Aktuell noch nicht vorhanden, Erstellung nach Vorgaben der Designer
Hinweis:
Dieses Briefing ist eine Kurzfassung. Gerne beantworten wir weitergehende Fragen.

```html
<!DOCTYPE html>
<html lang="de">
<head>
<meta charset="utf-8">
<title>norquavo – Praxisbegleitendes Coaching</title>
<link href="https://fonts.googleapis.com/css2?family=Signika:wght@400;600;700&family=Open+Sans:wght@400;600;700&display=swap" rel="stylesheet">
<style>
  :root{
    --green:#7dc12a;
    --grey:#80868a;
    --text:#5c6064;
    --stage:#4a4a4a;
    --paper:#ffffff;
  }
  *{margin:0;padding:0;box-sizing:border-box}
  html,body{width:890px;height:1200px;overflow:hidden;background:var(--stage)}
  body{position:relative;font-family:"Open Sans",sans-serif;color:var(--text)}
  .flyer-side{position:absolute;left:87px;width:943px;height:667px;background:var(--paper);
    transform:scale(.75);transform-origin:0 0;overflow:hidden;box-shadow:0 6px 14px rgba(0,0,0,.35)}
  .flyer-side.front{top:67px}
  .flyer-side.inside{top:606px}
  .shapes{position:absolute;inset:0;width:943px;height:667px}
  .abs{position:absolute}
  .brand{font-family:"Signika",sans-serif;font-weight:600;color:var(--grey);display:flex;align-items:center;gap:8px;line-height:1}
  .brand .dot{width:12px;height:12px;border-radius:50%;background:var(--green)}
  .brand-tag{font-size:10.5px;color:var(--grey);line-height:1.25;margin-left:20px;margin-top:4px;white-space:nowrap}
  .contact-head{font-weight:700;color:var(--green);font-size:11px}
  .contact-list{list-style:none;font-size:11.5px;white-space:nowrap}
  .contact-list li{display:flex;align-items:center;gap:10px;height:26.5px}
  .contact-list svg{width:10px;height:10px;flex:none}
  .contact-list .web{color:var(--green);font-weight:700}
  .portrait{width:90px;height:90px;border-radius:50%;border:4px solid var(--grey);box-shadow:0 0 0 3px var(--green) inset;
    background:radial-gradient(circle at 50% 40%,#c9c4be,#7d7f82)}
  .portrait-caption{font-size:10.5px;text-align:center;line-height:1.2;color:var(--text);white-space:nowrap}
  .portrait-caption b{font-weight:700}
  .values{font-size:9px;font-weight:700;color:var(--text);white-space:nowrap}
  .values .plus{color:var(--green)}
  .headline{font-family:"Signika",sans-serif;font-weight:700;font-size:43px;line-height:1.0;text-align:center;color:var(--grey);white-space:nowrap}
  .headline .accent{color:var(--green);display:block}
  .quote{font-size:11px;text-align:center;white-space:nowrap}
  .web-button{width:222px;height:30px;border-radius:15px;background:var(--green);color:#fff;
    font-family:"Signika",sans-serif;font-weight:700;font-size:17px;display:flex;align-items:center;justify-content:center;
    box-shadow:0 3px 4px rgba(0,0,0,.25)}
  .topics-title{font-family:"Signika",sans-serif;font-weight:700;font-size:22px;color:#fff}
  .topic-list{list-style:none;width:355px}
  .topic-list li{position:relative;height:32.3px;padding-left:29px;font-family:"Signika",sans-serif;font-weight:600;font-size:15px;color:var(--text);display:flex;align-items:center}
  .topic-list li::before{content:"";position:absolute;left:0;top:12px;width:9px;height:9px;border-radius:50%;background:var(--green)}
  .topic-list li::after{content:"";position:absolute;left:14px;right:0;bottom:2px;height:1px;background:var(--green)}
  .body-copy{font-size:11.2px;line-height:17px;white-space:nowrap}
  .body-copy p+p{margin-top:17px}
</style>
</head>
<body>

<section class="flyer-side front">
  <svg class="shapes" viewBox="0 0 943 667">
    <defs>
      <linearGradient id="team-photo" x1="0" y1="0" x2="1" y2="1">
        <stop offset="0" stop-color="#3c4670"/>
        <stop offset=".45" stop-color="#e6e8f0"/>
        <stop offset="1" stop-color="#6f86c2"/>
      </linearGradient>
    </defs>
    <path role="img" aria-label="Fotocollage: Geschäftsleute in Silhouette vor Stadtkulisse" d="M20,0 H943 V330 Q800,425 560,420 Q170,390 20,0 Z" fill="url(#team-photo)"/>
    <path d="M0,0 H28 Q170,400 560,425 Q800,430 943,335 V352 Q800,447 560,445 Q120,430 0,70 Z" fill="var(--green)"/>
    <polygon points="0,125 125,265 0,350" fill="var(--grey)"/>
    <polygon points="0,365 115,400 0,480" fill="var(--green)"/>
    <rect x="0" y="652" width="237" height="15" fill="var(--green)"/>
    <rect x="237" y="652" width="468" height="15" fill="var(--grey)"/>
    <rect x="705" y="652" width="238" height="15" fill="var(--green)"/>
  </svg>

  <div class="abs" style="left:535px;top:50px">
    <div class="brand" style="font-size:30px"><span class="dot"></span>norquavo</div>
    <div class="brand-tag" style="font-size:9px">Die richtigen Köpfe<br>gewinnen, fördern und binden</div>
  </div>

  <div class="abs" style="left:150px;top:410px">
    <div class="brand" style="font-size:38px"><span class="dot"></span>norquavo</div>
    <div class="brand-tag">Die richtigen Köpfe<br>gewinnen, fördern und binden</div>
  </div>

  <div class="abs" style="left:38px;top:495px;text-align:center">
    <div class="portrait" role="img" aria-label="Porträtfoto Berater"></div>
    <div class="portrait-caption" style="margin-top:6px;margin-left:-20px;width:130px"><b>Speicherviertel</b><br>Am Lotsenkai 14</div>
  </div>

  <div class="abs" style="left:153px;top:497px">
    <div class="contact-head">norquavo oHG</div>
    <ul class="contact-list" style="margin-top:4px">
      <li><svg viewBox="0 0 10 10"><circle cx="5" cy="5" r="5" fill="var(--green)"/><circle cx="5" cy="4" r="1.6" fill="#fff"/></svg>28817 Nordhafen</li>
      <li><svg viewBox="0 0 10 10"><circle cx="5" cy="5" r="5" fill="var(--green)"/><path d="M3,3 l1,0 1,1.5 -.7,.7 q.8,1.3 1.5,1.5 l.7,-.7 1.5,1 0,1 q-3,.3 -5,-5z" fill="#fff"/></svg>+49 (0) 40 555012-310/311</li>
      <li><svg viewBox="0 0 10 10"><circle cx="5" cy="5" r="5" fill="var(--green)"/><rect x="2.5" y="3.3" width="5" height="3.4" fill="#fff"/></svg>info@norquavo.com</li>
      <li class="web"><svg viewBox="0 0 10 10"><circle cx="5" cy="5" r="5" fill="var(--green)"/><circle cx="5" cy="5" r="2.5" fill="none" stroke="#fff" stroke-width=".9"/></svg>www.norquavo.com</li>
    </ul>
  </div>

  <div class="abs" style="left:346px;top:495px">
    <div class="portrait" role="img" aria-label="Porträtfoto Berater"></div>
    <div class="portrait-caption" style="margin-top:6px;margin-left:-20px;width:130px"><b>Jonas Hartwig</b><br>Lukas Brenner</div>
  </div>

  <div class="abs values" style="left:530px;top:458px">PROFESSIONELL <span class="plus">+</span> SYMPATHISCH <span class="plus">+</span> PRAKTISCH/PRAGMATISCH/ NATÜRLICH</div>
  <h1 class="abs headline" style="left:520px;top:474px;width:380px">Praxisbegleitendes<span class="accent">Coaching</span></h1>
  <p class="abs quote" style="left:520px;top:564px;width:380px">Wer zusieht, sieht mehr, als wer mitspielt“, Friedrich Lorenz.</p>
  <div class="abs web-button" style="left:596px;top:592px">www.norquavo.com</div>
</section>

<section class="flyer-side inside">
  <svg class="shapes" viewBox="0 0 943 667">
    <defs>
      <linearGradient id="network-photo" x1="0" y1="0" x2="1" y2="0">
        <stop offset="0" stop-color="#3b4f78"/>
        <stop offset=".55" stop-color="#c9d2e2"/>
        <stop offset="1" stop-color="#7a5a4a"/>
      </linearGradient>
      <radialGradient id="touch-photo" cx=".55" cy=".5" r=".6">
        <stop offset="0" stop-color="#c86a60"/>
        <stop offset=".45" stop-color="#3f4a60"/>
        <stop offset="1" stop-color="#24304a"/>
      </radialGradient>
    </defs>
    <path role="img" aria-label="Foto: Mann mit Brille vor digitaler Weltkugel mit Personensymbolen" d="M0,0 H505 Q430,160 240,190 Q100,205 0,175 Z" fill="url(#network-photo)"/>
    <path d="M505,0 H540 Q450,185 240,205 Q100,215 0,190 V175 Q100,205 240,190 Q430,160 505,0 Z" fill="var(--grey)"/>
    <path d="M555,0 H600 Q500,215 250,228 Q110,232 0,210 V190 Q100,215 240,205 Q450,185 555,0 Z" fill="var(--green)"/>
    <polygon points="62,205 262,198 284,274 42,290" fill="var(--green)"/>
    <path role="img" aria-label="Foto: Hand berührt digitales Netzwerk mit Bewerber-Symbolen" d="M490,175 Q600,60 720,0 H943 V265 Q850,290 700,268 Q560,245 490,175 Z" fill="url(#touch-photo)"/>
    <path d="M490,175 Q560,245 700,268 Q850,290 943,265 V283 Q850,305 700,290 Q560,265 490,175 Z" fill="var(--green)"/>
    <path d="M943,305 Q885,370 870,455 L943,480 Z" fill="var(--grey)"/>
    <polygon points="943,485 855,525 943,580" fill="var(--green)"/>
    <rect x="0" y="652" width="237" height="15" fill="var(--green)"/>
    <rect x="237" y="652" width="468" height="15" fill="var(--grey)"/>
    <rect x="705" y="652" width="238" height="15" fill="var(--green)"/>
  </svg>

  <h2 class="abs topics-title" style="left:68px;top:238px">Themenbeispiele:</h2>
  <ul class="abs topic-list" style="left:68px;top:297px">
    <li>Umgang mit Verschiedenheit</li>
    <li>Konfliktfähigkeit</li>
    <li>Prozessentwicklung/-optimierung</li>
    <li>Führungshandwerk</li>
    <li>Mitarbeiterführung</li>
    <li>Coaching</li>
    <li>Selbstmanagement</li>
    <li>Zeitmanagement</li>
    <li>Schlagfertigkeit</li>
    <li>Unternehmenskultur</li>
  </ul>

  <div class="abs" style="left:515px;top:306px">
    <div class="brand" style="font-size:38px"><span class="dot"></span>norquavo</div>
    <div class="brand-tag">Die richtigen Köpfe<br>gewinnen, fördern und binden</div>
  </div>

  <div class="abs body-copy" style="left:515px;top:391px">
    <p>Als „Schatten im Hintergrund“ wird der Coachee<br>(Führungskraft/ Mitarbeiter) im gewohnten Arbeitsumfeld<br>während der Ausübung seiner beruflichen Tätigkeit vom<br>Coach begleitet. Anschließend erhält er eine unmittelbare<br>Rückmeldung zu seiner Kommunikations- und<br>Interaktionsweise bei konkreten Situationen im Arbeitsalltag.</p>
    <p>Ziel des Coachings ist es, über Rückmeldung und Reflexion<br>Einstellungs- und Verhaltensänderungen zu initiieren,<br>um die persönliche Wirksamkeit zu steigern.</p>
  </div>

  <div class="abs web-button" style="left:596px;top:587px">www.norquavo.com</div>
</section>

</body>
</html>
```